I need to redesign this website. Modern Fun Professional Redesign For www.JollyPerkHub.com = New Name www.ClaimVouchly.com

Use existing content as it is on website exactly and we will revise after initial mock ups.

The new name will be ClaimVouchly.com please make a quick logo for this site too while redesigning.

Make it look like an official website....

Target Market(s)

Consumers that are redeeming certificates that businesses gave to them as a gift for customer loyalty,e tc.

Industry/Entity Type

It Professional

Logo Text

www.ClaimVouchly.com

Number of Pages Required

4 page

Colors

Designer to choose colors to be used in the design.

Requirements
Must have
• Must look professional, build trust and credibility.
Nice to have
• open
Should not have
• open

```html
<!DOCTYPE html>
<html lang="en">
<head>
<meta charset="utf-8">
<title>ClaimVouchly.com – Dining Incentive Certificates</title>
<link href="https://fonts.googleapis.com/css2?family=Ubuntu:wght@300;400;500;700&display=swap" rel="stylesheet">
<style>
  :root {
    --tab-grey: #a3a3a3;
    --tab-active: #0e6077;
    --heading-green: #7aab12;
    --title-teal: #10403f;
    --body-grey: #6b6b6b;
    --muted-grey: #9a9a9a;
    --ink: #1c1c1c;
    --card-border: #333333;
    --icon-green: #1c6b2c;
    --button-text: #1c6b2c;
    --page-bg: #ffffff;
  }
  * { margin: 0; padding: 0; box-sizing: border-box; }
  html, body { width: 1200px; height: 501px; overflow: hidden; background: var(--page-bg); }
  body { position: relative; font-family: "Ubuntu", sans-serif; }

  .category-nav a {
    position: absolute; top: 0; height: 31px;
    background: var(--tab-grey); color: #fff;
    font-size: 11.5px; font-weight: 300; text-decoration: none; white-space: nowrap;
    display: flex; align-items: center; justify-content: center;
    border-radius: 0 0 2px 2px;
  }
  .category-nav a.is-active { background: var(--tab-active); }

  .see-all {
    position: absolute; top: 49px; left: 0; width: 1200px;
    text-align: center; font-size: 20px; font-weight: 300;
    color: var(--muted-grey); letter-spacing: .5px;
  }
  .section-title {
    position: absolute; top: 84px; left: 0; width: 1200px;
    text-align: center; font-size: 43px; font-weight: 500;
    color: var(--heading-green);
  }

  .certificate-card {
    position: absolute; top: 158px; width: 260px; height: 261px;
    border: 1px solid var(--card-border);
  }
  .certificate-card h3 {
    position: absolute; top: 12px; font-size: 19px; font-weight: 500;
    line-height: 20px; color: var(--title-teal); white-space: nowrap;
  }
  .certificate-card .tagline {
    position: absolute; top: 55px; font-size: 10px; font-weight: 700;
    color: var(--title-teal); white-space: nowrap;
  }
  .certificate-card .description {
    position: absolute; top: 70px; width: 226px;
    font-size: 13px; font-weight: 300; line-height: 18px; letter-spacing: -.1px;
    color: var(--body-grey); text-align: justify;
  }
  .certificate-card .more-info {
    position: absolute; top: 198px; width: 110px; height: 22px;
    border: 1px solid var(--card-border); color: var(--button-text);
    font-size: 10.5px; font-weight: 400; text-decoration: none; white-space: nowrap;
    display: flex; align-items: center; padding-left: 12px;
  }
  .certificate-card .print-link {
    position: absolute; font-size: 10.5px; line-height: 15.5px; color: var(--ink); white-space: nowrap;
  }
  .certificate-card .dining-icon { position: absolute; top: 194px; width: 28px; height: 28px; }
  .certificate-card .photo { position: absolute; top: 177px; width: 76px; height: 81px; }
  .photo-dining-room { background: linear-gradient(160deg, #6b3a1c 0%, #a76a33 45%, #3e200f 100%); }
  .photo-plated-meal { background: linear-gradient(180deg, #8a6a4a 0%, #d9c8b0 55%, #f1ece4 80%, #0f4d16 80%, #0f4d16 100%); }

  .more-certificates {
    position: absolute; top: 439px; left: 0; width: 1200px;
    text-align: center; font-size: 8.5px; font-weight: 700; color: var(--ink);
  }
  .pager { position: absolute; top: 455px; left: 554px; width: 94px; height: 16px; }
</style>
</head>
<body>
  <nav class="category-nav">
    <a href="#" style="left:248px;width:86px">VACATIONS</a>
    <a href="#" style="left:346px;width:137px">ELECTRONIC PRODUCT</a>
    <a href="#" class="is-active" style="left:495px;width:138px">DINING CERTIFICATES</a>
    <a href="#" style="left:642px;width:150px">GAS &amp; GROCERY REBATE</a>
    <a href="#" style="left:801px;width:151px">DISCOUNT CERTIFICATES</a>
  </nav>

  <p class="see-all">SEE ALL OUR CERTIFICATES</p>
  <h1 class="section-title">Dinning incentive certificates</h1>

  <article class="certificate-card" style="left:335px">
    <h3 style="left:21px">Premium $25 Restaurant<br>Gift Certificate</h3>
    <p class="tagline" style="left:21px">Three electronic products in one!</p>
    <p class="description" style="left:22px">Receive $25 off their bill at any of our participating restaurants. We currently feature thousands of participating restaurants, nationwide. Take a time and visit all our participating restau&shy;rants in your area.</p>
    <a href="#" class="more-info" style="left:20px">More Information</a>
    <svg class="dining-icon" style="left:141px" viewBox="0 0 28 28" aria-hidden="true">
      <circle cx="14" cy="14" r="12.5" fill="none" stroke="var(--icon-green)" stroke-width="2"/>
      <circle cx="14" cy="14" r="9.5" fill="none" stroke="var(--icon-green)" stroke-width="1.4"/>
      <path d="M10 8v5a1.5 1.5 0 0 0 3 0V8M11.5 13v7M17 8c-1.5 1-1.5 5 0 6v6" fill="none" stroke="var(--icon-green)" stroke-width="1.4" stroke-linecap="round"/>
    </svg>
    <div class="photo photo-dining-room" style="left:182px" role="img" aria-label="Restaurant dining room with set tables and wooden chairs"></div>
    <p class="print-link" style="left:21px;top:223px">Click Here To Print &amp;<br>Email Sample Certificates.</p>
  </article>

  <article class="certificate-card" style="left:604px">
    <h3 style="left:22px;top:15px">$300 Restaurant<br>Certificate</h3>
    <p class="tagline" style="left:22px;top:56px">Many Restaurants disposed for you</p>
    <p class="description" style="left:21px">Receive $25 off their bill at any of our participating restaurants. We currently feature thousands of participating restaurants, nationwide. Take a time and visit all our participating restau&shy;rants in your area.</p>
    <a href="#" class="more-info" style="left:20px">More Information</a>
    <svg class="dining-icon" style="left:148px" viewBox="0 0 28 28" aria-hidden="true">
      <circle cx="14" cy="14" r="12.5" fill="none" stroke="var(--icon-green)" stroke-width="2"/>
      <circle cx="14" cy="14" r="9.5" fill="none" stroke="var(--icon-green)" stroke-width="1.4"/>
      <path d="M10 8v5a1.5 1.5 0 0 0 3 0V8M11.5 13v7M17 8c-1.5 1-1.5 5 0 6v6" fill="none" stroke="var(--icon-green)" stroke-width="1.4" stroke-linecap="round"/>
    </svg>
    <div class="photo photo-plated-meal" style="left:182px" role="img" aria-label="Plated gourmet meal on a white table setting"></div>
    <p class="print-link" style="left:21px;top:229px">Click Here To Print &amp;<br>Email Sample Certificates.</p>
  </article>

  <p class="more-certificates">View More certificates</p>
  <svg class="pager" viewBox="0 0 94 16" aria-label="Certificate pages">
    <path d="M7 1 2 8l5 7" fill="none" stroke="var(--ink)" stroke-width="1.2"/>
    <rect x="19" y="2" width="13" height="12" rx="2" fill="#c4c4c4"/>
    <text x="25.5" y="11.5" font-family="Ubuntu, sans-serif" font-size="9" font-weight="700" text-anchor="middle" fill="var(--ink)">1</text>
    <rect x="41" y="2" width="12" height="12" rx="2" fill="#b3b3b3"/>
    <text x="47" y="11.5" font-family="Ubuntu, sans-serif" font-size="9" text-anchor="middle" fill="#fff">2</text>
    <rect x="62" y="2" width="13" height="12" rx="2" fill="#b3b3b3"/>
    <text x="68.5" y="11.5" font-family="Ubuntu, sans-serif" font-size="9" text-anchor="middle" fill="#fff">3</text>
    <path d="M85 1l5 7-5 7" fill="none" stroke="var(--ink)" stroke-width="1.2"/>
  </svg>
</body>
</html>
```